teaching love. a joyful state of being.

adding value to ones circumstance through the teachings of neutralization. quote for back of card: "and then it happens... One day you wake up and you're in this place. You are in this place where everything is right. Your heart is calm. Your soul is lit. Your thoughts are positive. Your vision is clear. Your faith is stronger than ever. And you are at peace. At peace with where you have been. At peace with what you've been through. And at peace with where you're headed." -unknown

Target Market(s)

spiritual, awakening, inspiration, motivation, gratefulness, oneness, peace, positive mindset,

Contact Information for Business Card

front: one line message from quote

Logo Text

up to suggestions

Font styles to use
Serif
Sans Serif
Script

Colors

Designer to choose colors to be used in the design.

Requirements
Must have
• entire quote on one side of card
Nice to have
• simple, and to the point
Should not have
• elaborated designs

```html
<!DOCTYPE html>
<html lang="en">
<head>
<meta charset="utf-8">
<title>Business Card – Front and Back</title>
<link rel="stylesheet" href="https://fonts.googleapis.com/css2?family=Noto+Serif:wght@400&family=Open+Sans:wght@400;500&display=swap">
<style>
  :root {
    --red: #e8191c;
    --dark-red: #8e0c0e;
    --black: #0b0b0b;
    --white: #ffffff;
    --grey-text: #555555;
    --backdrop: #e4e4e4;
    --serif: "Noto Serif", Georgia, serif;
    --sans: "Open Sans", Verdana, sans-serif;
  }
  * { margin: 0; padding: 0; box-sizing: border-box; }
  html, body {
    width: 1200px;
    height: 774px;
    overflow: hidden;
    background: var(--backdrop);
  }
  .canvas {
    position: relative;
    width: 1200px;
    height: 774px;
  }
  .card {
    position: absolute;
    top: 227px;
    width: 560px;
    height: 320px;
    background: var(--white);
    overflow: hidden;
    box-shadow: 0 6px 18px rgba(0,0,0,0.18);
  }
  .card--back { left: 20px; }
  .card--front { left: 620px; }
  .card__shapes {
    position: absolute;
    inset: 0;
  }

  /* Back */
  .quote {
    position: absolute;
    top: 48px;
    left: 26px;
    right: 26px;
    font-family: var(--sans);
    font-weight: 500;
    font-size: 19px;
    line-height: 1.32;
    color: var(--red);
    text-align: center;
  }

  /* Front */
  .logo-placeholder {
    position: absolute;
    left: 30px;
    top: 132px;
    width: 240px;
    font-family: var(--serif);
    font-size: 32px;
    line-height: 1.2;
    color: var(--red);
    text-align: center;
  }
  .identity {
    position: absolute;
    right: 26px;
    top: 92px;
    text-align: right;
  }
  .identity__name {
    font-family: var(--serif);
    font-size: 28px;
    color: var(--grey-text);
    line-height: 1.1;
  }
  .identity__role {
    font-family: var(--serif);
    font-size: 19px;
    color: var(--red);
    line-height: 1.1;
  }
  .contact-line {
    position: absolute;
    left: 346px;
    font-family: var(--serif);
    color: var(--white);
    white-space: nowrap;
    line-height: 28px;
    height: 28px;
  }
  .contact-line--address { top: 166px; font-size: 19px; }
  .contact-line--phone { top: 212px; font-size: 19px; }
  .contact-line--email { top: 258px; font-size: 12.5px; }
</style>
</head>
<body>
<main class="canvas">

  <section class="card card--back" aria-label="Card back">
    <svg class="card__shapes" width="560" height="320" viewBox="0 0 560 320" aria-hidden="true">
      <rect class="accent-rule" x="250" y="22" width="60" height="4" fill="var(--red)"/>
    </svg>
    <p class="quote">and then it happens... One day you wake up and you're in this place. You are in this place where everything is right. Your heart is calm. Your soul is lit. Your thoughts are positive. Your vision is clear. Your faith is stronger than ever. And you are at peace. At peace with where you have been. At peace with what you've been through. And at peace with where you're headed.</p>
  </section>

  <section class="card card--front" aria-label="Card front">
    <svg class="card__shapes" width="560" height="320" viewBox="0 0 560 320" aria-hidden="true">
      <rect class="accent-band" x="380" y="0" width="180" height="10" fill="var(--red)"/>
      <rect x="300" y="152" width="260" height="168" fill="var(--black)"/>
      <g>
        <rect x="310" y="166" width="228" height="28" fill="var(--red)"/>
        <rect x="538" y="166" width="14" height="28" fill="var(--dark-red)"/>
        <rect x="310" y="212" width="228" height="28" fill="var(--red)"/>
        <rect x="538" y="212" width="14" height="28" fill="var(--dark-red)"/>
        <rect x="310" y="258" width="228" height="28" fill="var(--red)"/>
        <rect x="538" y="258" width="14" height="28" fill="var(--dark-red)"/>
      </g>
      <g fill="none" stroke="var(--white)" stroke-width="1.4">
        <path class="icon-pin" d="M328 189 C322 182 320 178 320 175 A8 8 0 0 1 336 175 C336 178 334 182 328 189 Z"/>
        <circle cx="328" cy="175" r="2.5"/>
        <rect class="icon-phone" x="323" y="216" width="10" height="20" rx="2"/>
        <line x1="326" y1="233" x2="330" y2="233"/>
        <rect class="icon-mail" x="319" y="265" width="18" height="14"/>
        <polyline points="319,265 328,273 337,265"/>
      </g>
    </svg>

    <div class="logo-placeholder">Your LOGO<br>Goes Here</div>

    <div class="identity">
      <p class="identity__name">Amani Wanjiru</p>
      <p class="identity__role">Manager</p>
    </div>

    <p class="contact-line contact-line--address">48 Riverside Lane</p>
    <p class="contact-line contact-line--phone">+254 700 123456</p>
    <p class="contact-line contact-line--email">amani.wanjiru@example.com</p>
  </section>

</main>
</body>
</html>
```